Gummy Label design for hemp company

I need a 3.25 inch wide by 4 inch tall label made to be put on bags of gummies. I will include all disclaimers that need to be there, as well as my logo. This is for our 25 mg Delta 8 gummies 20ct, but I will use the design for our entire gummy line, just editing the text. Needs to have ingredient list. Ingredients: Sugar, Inulin, Corn syrup, water, pectin, citric acid, baking soda, fruit, hemp extract.

Everything should be on one label as this is going on a sticker that will be placed on a bag.
I would like to highlight that they are vegan if possible.

• Must have the following disclaimer: "Contains Farm Bill compliant hemp extract. These statements have not been evaluated by the QVR. This product is NOT intended to treat, cure, or prevent any disease. Do not operate heavy machinery while using this product. This product may cause you to fail a drug test. Consult with your doctor before trying any new products. Do not take if pregnant or lactating. If you experience any adverse effects, discontinue use and seek advice from your physician."
• NEEDS TO SAY: "100% hemp derived" also "<.3% D9 THC"

```html
<!DOCTYPE html>
<html lang="en">
<head>
<meta charset="utf-8">
<title>Brightleaf Hemp – Gummy Labels</title>
<link rel="stylesheet" href="https://fonts.googleapis.com/css2?family=Nunito:wght@800&family=Tinos:ital@0;1&family=Arimo:wght@400;700&family=Berkshire+Swash&display=swap">
<style>
  :root{
    --forest:#3f7636;
    --lime:#a3bd3a;
    --lime-soft:#eef3d4;
    --paper:#ffffff;
    --ink:#222222;
    --pill:#1c1c1c;
    --stage:#f4f4f4;
  }
  *{box-sizing:border-box;margin:0;padding:0}
  html,body{width:1200px;height:1200px;overflow:hidden;background:var(--stage)}
  .stage{position:relative;width:1200px;height:1200px;display:flex;gap:40px;justify-content:center;align-items:center}
  .label{position:relative;width:540px;height:664px;overflow:hidden}
  .label > svg.bg{position:absolute;inset:0}
  .abs{position:absolute}

  .brand{left:0;right:0;text-align:center;font-family:"Nunito",sans-serif;font-weight:800}
  .brand-mark{width:58px;height:58px;left:241px;top:62px}
  .brand-name{top:138px;font-size:62px;line-height:1;letter-spacing:-1px}
  .brand-sub{top:210px;font-size:30px;letter-spacing:18px;padding-left:120px;line-height:1}

  /* green label */
  .label--green{background:var(--lime)}
  .label--green .brand{color:var(--paper)}
  .label--green .brand-mark{background:var(--paper)}
  .ingredients-box{left:22px;top:400px;width:198px;height:132px;background:var(--forest);border-radius:12px;padding:12px 14px;color:var(--paper)}
  .ingredients-box h3{font-family:"Arimo",sans-serif;font-weight:700;font-size:17px;padding-bottom:3px;border-bottom:1.5px solid var(--lime);margin-bottom:5px}
  .ingredients-box p{font-family:"Tinos",serif;font-size:15px;line-height:1.28}
  .thc-note{left:22px;width:198px;top:548px;text-align:center;font-family:"Tinos",serif;font-size:17px;line-height:1.3;color:var(--lime-soft)}
  .thc-note em{font-style:italic}
  .disclaimer-box{left:240px;top:400px;width:282px;height:202px;border:1.5px solid rgba(255,255,255,.65);border-radius:12px;padding:8px 10px 8px 12px;list-style:none}
  .disclaimer-box li{position:relative;padding-left:17px;font-family:"Tinos",serif;font-size:11.3px;line-height:1.25;color:var(--paper);margin-bottom:5px}
  .disclaimer-box li svg{position:absolute;left:0;top:1px;width:11px;height:11px}
  .footer-band{left:0;right:0;top:622px;height:42px;background:var(--forest);color:var(--paper);font-family:"Tinos",serif;font-size:13px;line-height:1.3;text-align:center;padding-top:4px}

  /* white label */
  .label--white{background:var(--paper);border:1px solid #555}
  .label--white .brand{color:var(--forest)}
  .label--white .brand-mark{background:var(--forest);top:30px}
  .label--white .brand-name{top:108px}
  .label--white .brand-sub{top:180px;color:var(--forest)}
  .disclaimer-list{left:18px;top:392px;width:268px;list-style:none}
  .disclaimer-list li{font-family:"Tinos",serif;font-size:11.5px;line-height:1.22;color:var(--ink);padding:1px 8px 2px 14px;border-left:1.5px solid var(--lime);border-bottom:1.5px solid var(--lime);margin-bottom:4px}
  .badge{left:292px;top:382px;width:222px;height:222px}
  .badge svg{position:absolute;inset:0}
  .badge-text{position:absolute;left:30px;right:30px;top:46px;text-align:center;color:var(--paper)}
  .badge-text h3{font-family:"Berkshire Swash",cursive;font-weight:400;font-size:21px;margin-bottom:2px}
  .badge-text p{font-family:"Arimo",sans-serif;font-size:14.5px;line-height:1.22}
  .footer-pill{left:56px;top:608px;width:420px;height:42px;border-radius:21px;background:var(--pill);color:var(--paper);font-family:"Arimo",sans-serif;font-size:12.5px;line-height:1.3;text-align:center;padding-top:4px}
</style>
</head>
<body>
<main class="stage">

  <!-- Green variant -->
  <section class="label label--green">
    <svg class="bg" viewBox="0 0 540 664" width="540" height="664">
      <path d="M0 0H540V272C420 400 150 400 0 305Z" fill="var(--paper)"/>
      <path d="M0 0H540V246C400 360 130 360 0 230Z" fill="var(--forest)"/>
    </svg>
    <div class="brand abs brand-mark"></div>
    <div class="brand abs brand-name">Brightleaf</div>
    <div class="brand abs brand-sub">HEMP</div>

    <div class="ingredients-box abs">
      <h3>Ingredients:</h3>
      <p>Sugar, Inulin, Corn syrup, water, pectin, citric acid, baking soda, fruit, hemp extract.</p>
    </div>
    <p class="thc-note abs"><em>100% hemp derived</em><br>also<br><em>&lt;.3% D9 THC</em></p>

    <ul class="disclaimer-box abs">
      <li><svg viewBox="0 0 12 12"><path d="M1.5 6.5 5 9.5 10.5 2.5" fill="none" stroke="var(--forest)" stroke-width="2"/></svg>Contains Farm Bill compliant hemp extract.</li>
      <li><svg viewBox="0 0 12 12"><path d="M1.5 6.5 5 9.5 10.5 2.5" fill="none" stroke="var(--forest)" stroke-width="2"/></svg>These statements have not been evaluated by the QVR.</li>
      <li><svg viewBox="0 0 12 12"><path d="M1.5 6.5 5 9.5 10.5 2.5" fill="none" stroke="var(--forest)" stroke-width="2"/></svg>This product is NOT intended to treat, cure, or prevent any disease.</li>
      <li><svg viewBox="0 0 12 12"><path d="M1.5 6.5 5 9.5 10.5 2.5" fill="none" stroke="var(--forest)" stroke-width="2"/></svg>Do not operate heavy machinery while using this product.</li>
      <li><svg viewBox="0 0 12 12"><path d="M1.5 6.5 5 9.5 10.5 2.5" fill="none" stroke="var(--forest)" stroke-width="2"/></svg>This product may cause you to fail a drug test.</li>
      <li><svg viewBox="0 0 12 12"><path d="M1.5 6.5 5 9.5 10.5 2.5" fill="none" stroke="var(--forest)" stroke-width="2"/></svg>Consult with your doctor before trying any new products.</li>
      <li><svg viewBox="0 0 12 12"><path d="M1.5 6.5 5 9.5 10.5 2.5" fill="none" stroke="var(--forest)" stroke-width="2"/></svg>Do not take if pregnant or lactating.</li>
    </ul>

    <p class="footer-band abs">“If you experience any adverse effects, discontinue use and<br>seek advice from your physician.”</p>
  </section>

  <!-- White variant -->
  <section class="label label--white">
    <svg class="bg" viewBox="0 0 540 664" width="540" height="664">
      <path d="M0 200C140 300 400 300 540 200C400 380 140 380 0 200Z" fill="var(--lime)"/>
      <path d="M0 200C140 300 400 300 540 200C400 320 140 320 0 200Z" fill="var(--forest)"/>
      <defs><path id="arc-line" d="M95 300Q270 405 445 300"/></defs>
      <text font-family="Nunito, sans-serif" font-weight="800" font-size="17" fill="var(--ink)">
        <textPath href="#arc-line" startOffset="50%" text-anchor="middle">100% hemp derived also &lt;.3% D9 THC</textPath>
      </text>
    </svg>
    <div class="brand abs brand-mark"></div>
    <div class="brand abs brand-name">Brightleaf</div>
    <div class="brand abs brand-sub">HEMP</div>

    <ul class="disclaimer-list abs">
      <li>Contains Farm Bill compliant hemp extract.</li>
      <li>These statements have not been evaluated by the QVR.</li>
      <li>This product is NOT intended to treat, cure, or prevent any disease.</li>
      <li>Do not operate heavy machinery while using this product.</li>
      <li>This product may cause you to fail a drug test.</li>
      <li>Consult with your doctor before trying any new products.</li>
      <li>Do not take if pregnant or lactating.</li>
    </ul>

    <div class="badge abs">
      <svg viewBox="0 0 100 100">
        <polygon transform="translate(4 2) rotate(6 50 50)" fill="var(--lime)" points="100,50 92.7,58.5 96.2,69.1 86.2,74.2 85.4,85.4 74.2,86.2 69.1,96.2 58.5,92.7 50,100 41.5,92.7 30.9,96.2 25.8,86.2 14.6,85.4 13.8,74.2 3.8,69.1 7.3,58.5 0,50 7.3,41.5 3.8,30.9 13.8,25.8 14.6,14.6 25.8,13.8 30.9,3.8 41.5,7.3 50,0 58.5,7.3 69.1,3.8 74.2,13.8 85.4,14.6 86.2,25.8 96.2,30.9 92.7,41.5"/>
        <polygon fill="var(--forest)" points="100,50 92.7,58.5 96.2,69.1 86.2,74.2 85.4,85.4 74.2,86.2 69.1,96.2 58.5,92.7 50,100 41.5,92.7 30.9,96.2 25.8,86.2 14.6,85.4 13.8,74.2 3.8,69.1 7.3,58.5 0,50 7.3,41.5 3.8,30.9 13.8,25.8 14.6,14.6 25.8,13.8 30.9,3.8 41.5,7.3 50,0 58.5,7.3 69.1,3.8 74.2,13.8 85.4,14.6 86.2,25.8 96.2,30.9 92.7,41.5"/>
      </svg>
      <div class="badge-text">
        <h3>Ingredients:</h3>
        <p>Sugar, Inulin,<br>Corn syrup, water,<br>pectin, citric acid,<br>baking soda, fruit,<br>hemp extract.</p>
      </div>
    </div>

    <p class="footer-pill abs">"If you experience any adverse effects, discontinue use and<br>seek advice from your physician."</p>
  </section>

</main>
</body>
</html>
```